Upscale business cards needed for family office

We would like professional business cards created for employees of our family office. Relatively simple and straightforward, but also with a unique element to set them apart. Probably stick with neutral and simple colors that mesh well with the colors in the logo. We need space for the traditional elements, including name, title, address, email/phone number.

Industry/Entity Type

Business

Contact Information for Business Card

Space for name, title, phone number, email, address

```html
<!DOCTYPE html>
<html lang="en">
<head>
<meta charset="utf-8">
<title>H&amp;V Business Cards</title>
<link href="https://fonts.googleapis.com/css2?family=Quicksand:wght@500;700&display=swap" rel="stylesheet">
<style>
  :root {
    --backdrop: #6b6c6e;
    --card: #ffffff;
    --navy: #143f6e;
    --blue: #1277bf;
    --rule-grey: #a9abae;
    --mark-grey: #5f6669;
    --frame-grey: #b9bbbd;
    --ink-light: #ffffff;
  }
  * { margin: 0; padding: 0; box-sizing: border-box; }
  html, body { width: 1200px; height: 848px; overflow: hidden; }
  body {
    background: var(--backdrop);
    font-family: "Quicksand", sans-serif;
    position: relative;
  }
  .card {
    position: absolute;
    background: var(--card);
    overflow: hidden;
  }
  .card--front { left: 71px; top: 37px; width: 717px; height: 379px; }
  .card--back { left: 428px; top: 430px; width: 724px; height: 400px; }

  .brand-frame {
    position: absolute;
    background: var(--card);
    border: 4px solid var(--frame-grey);
    display: flex;
    align-items: center;
    justify-content: center;
    z-index: 2;
  }
  .brand-name {
    font-family: "Quicksand", sans-serif;
    font-weight: 700;
    color: var(--mark-grey);
    letter-spacing: 1px;
  }
  .card--front .brand-frame { left: 289px; top: 37px; width: 134px; height: 143px; }
  .card--front .brand-name { font-size: 40px; }
  .card--back .brand-frame { left: 285px; top: 104px; width: 167px; height: 184px; }
  .card--back .brand-name { font-size: 50px; }

  .front-band {
    position: absolute; left: 0; top: 219px; width: 100%; height: 29px;
    background: var(--navy);
  }
  .front-notch {
    position: absolute; left: 303px; top: 219px; right: 0; height: 9px;
    background: var(--card);
    border-left: 3px solid var(--rule-grey);
    border-bottom: 3px solid var(--rule-grey);
  }
  .contact-panel {
    position: absolute; left: 0; top: 248px; width: 100%; height: 131px;
    background: var(--blue);
    border-top: 1px solid #4f9ad3;
  }
  .contact-row {
    position: absolute;
    display: flex; align-items: center; gap: 14px;
    color: var(--ink-light);
    font-size: 14px; font-weight: 700;
  }
  .contact-row svg { width: 20px; height: 20px; flex: none; }
  .contact-row--name { left: 36px; top: 14px; }
  .contact-row--phone { left: 36px; top: 46px; }
  .contact-row--address { left: 36px; top: 82px; }
  .contact-row--email { left: 36px; top: 110px; }
  .contact-row--web { right: 12px; top: 110px; }

  .back-rule {
    position: absolute; left: 0; top: 241px; width: 281px; height: 12px;
    background: var(--rule-grey);
  }
  .back-band {
    position: absolute; left: 0; top: 264px; width: 100%; height: 44px;
    background: var(--navy);
  }
</style>
</head>
<body>

<section class="card card--front">
  <div class="brand-frame"><span class="brand-name">H&amp;V</span></div>
  <div class="front-band"></div>
  <div class="front-notch"></div>
  <div class="contact-panel">
    <div class="contact-row contact-row--name">
      <svg viewBox="0 0 20 20" fill="none" stroke="#fff" stroke-width="2.2"><circle cx="10" cy="6" r="3.5"/><path d="M3 17c0-4 3.2-6 7-6s7 2 7 6z"/></svg>
      <span>Lena Marsh</span>
    </div>
    <div class="contact-row contact-row--phone">
      <svg viewBox="0 0 20 20" fill="#fff"><path d="M5 2l3 1 1 4-2 1.5c1 2 2.5 3.5 4.5 4.5L13 11l4 1 1 3-2 2C9 17 3 11 3 4z"/></svg>
      <span>555-012</span>
    </div>
    <div class="contact-row contact-row--address">
      <svg viewBox="0 0 20 20" fill="none" stroke="#fff" stroke-width="2.2"><path d="M10 19s-6-6.5-6-11a6 6 0 0 1 12 0c0 4.5-6 11-6 11z"/><circle cx="10" cy="8" r="2"/></svg>
      <span>Elm Road, USA</span>
    </div>
    <div class="contact-row contact-row--email">
      <svg viewBox="0 0 20 20" fill="#fff"><rect x="2" y="4" width="16" height="12" rx="1"/><path d="M3 5l7 6 7-6" fill="none" stroke="#1277bf" stroke-width="1.6"/></svg>
      <span>lenamarsh@mailbox.com</span>
    </div>
    <div class="contact-row contact-row--web">
      <svg viewBox="0 0 20 20" fill="none" stroke="#fff" stroke-width="1.6"><circle cx="10" cy="10" r="8"/><ellipse cx="10" cy="10" rx="3.5" ry="8"/><path d="M2 10h16M3.5 6h13M3.5 14h13"/></svg>
      <span>www.lenamarsh.com</span>
    </div>
  </div>
</section>

<section class="card card--back">
  <div class="back-rule"></div>
  <div class="back-band"></div>
  <div class="brand-frame"><span class="brand-name">H&amp;V</span></div>
</section>

</body>
</html>
```